Brand new leaflet design creative ideas.

I need a flyer designed for my business

I run a pay weekly carpet business and need designs for a flyer this design i will also want to enable it on letterheads business cards and a logo from it when created.

my domain name is www.pallowmere.co.uk / www.pallowmere.com

Our main competitor i have attached his design to this brief to give you a bit of an idea on how we work, however i do not want a copycat design i want a brand new design something not like theres but eye catching direct to the point.

We are open to colour suggestions as long as the colours work.
Thank you.

Target Market(s)

This print material will be delivered to customers houses.

Industry/Entity Type

Flooring

Font styles to use
Serif
Sans Serif

Requirements
Must have
• Website domain name,
• Various print options CMYK, PDF
Nice to have
• Creativity eye catching
Should not have
• SHOULD NOT BE A COPYCAT DESIGN SOMETHING NEW & CREATIVE

```html
<!DOCTYPE html>
<html lang="en">
<head>
<meta charset="utf-8">
<title>Pallowmere – Pay Weekly Carpet &amp; Vinyls Flyer</title>
<link rel="stylesheet" href="https://fonts.googleapis.com/css2?family=Bowlby+One&family=Cinzel:wght@600;700&family=Lobster&family=Open+Sans:wght@400;600;700&family=Oswald:wght@400;500&family=Permanent+Marker&display=swap">
<style>
  :root {
    --backdrop: #8a8a8a;
    --paper: #e6e7e8;
    --red: #e2262b;
    --red-warm: #e33e2c;
    --yellow: #fbe600;
    --yellow-soft: #f5e45a;
    --wine: #8e1b1b;
    --ink: #111111;
    --white: #ffffff;
  }
  html, body {
    margin: 0;
    padding: 0;
    width: 962px;
    height: 1200px;
    overflow: hidden;
    background: var(--backdrop);
  }
  .flyer {
    position: absolute;
    left: 45px;
    top: 0;
    width: 872px;
    height: 1200px;
    display: block;
  }
  .paper { fill: var(--paper); }
  .tile-red { fill: var(--red); }
  .tile-red-warm { fill: var(--red-warm); }
  .tile-yellow { fill: var(--yellow); }
  .tile-yellow-soft { fill: var(--yellow-soft); }
  .tile-gap { stroke: var(--paper); stroke-width: 7; }

  .corner-offer { font-family: "Open Sans", sans-serif; font-weight: 700; font-size: 44px; letter-spacing: -1.5px; }
  .corner-offer--white { fill: var(--white); }
  .corner-offer--yellow { fill: var(--yellow); }

  .share-note { font-family: "Cinzel", serif; font-weight: 700; text-anchor: end; }
  .share-note--lead { fill: var(--wine); font-size: 40px; }
  .share-note--lead .or { fill: var(--ink); }
  .share-note--follow { fill: var(--ink); font-size: 31px; font-weight: 600; }

  .title-band { fill: rgba(30, 20, 15, 0.72); }
  .title-pay { font-family: "Cinzel", serif; font-weight: 700; font-size: 68px; fill: var(--white); }
  .title-carpet { font-family: "Bowlby One", sans-serif; font-size: 78px; fill: var(--yellow); }
  .title-vinyls { font-family: "Lobster", cursive; font-size: 58px; fill: var(--yellow); }

  .brand-name { font-family: "Open Sans", sans-serif; font-weight: 700; font-size: 50px; fill: var(--red); }

  .welcome { font-family: "Oswald", sans-serif; font-weight: 400; font-size: 46px; fill: #c4302b; text-anchor: middle; }
  .area { font-family: "Oswald", sans-serif; font-weight: 500; font-size: 36px; fill: var(--ink); text-anchor: middle; }

  .urgent { font-family: "Permanent Marker", cursive; font-size: 40px; fill: var(--white); }
  .save-today { font-family: "Open Sans", sans-serif; font-weight: 700; font-style: italic; font-size: 26px; fill: var(--yellow); letter-spacing: 1px; }

  .deals-heading { font-family: "Open Sans", sans-serif; font-weight: 600; font-size: 45px; fill: var(--red); }
  .deals-side { font-family: "Open Sans", sans-serif; font-weight: 600; font-size: 34px; fill: var(--ink); }
  .deal-item { font-family: "Open Sans", sans-serif; font-weight: 400; font-size: 30px; fill: var(--ink); }
  .deal-item .strong { font-weight: 700; }
  .deal-tick { fill: none; stroke: var(--red); stroke-width: 2; stroke-linecap: round; stroke-linejoin: round; }

  .contact-label { font-family: "Oswald", sans-serif; font-weight: 400; font-size: 22px; fill: var(--white); }
  .contact-phone { font-family: "Oswald", sans-serif; font-weight: 500; font-size: 33px; fill: var(--ink); letter-spacing: 1px; }
  .contact-web { font-family: "Open Sans", sans-serif; font-weight: 600; font-size: 25px; fill: var(--ink); letter-spacing: 1px; }
</style>
</head>
<body>
<svg class="flyer" viewBox="0 0 867 1195" xmlns="http://www.w3.org/2000/svg">
  <defs>
    <linearGradient id="carpet-tones" x1="0" y1="0" x2="0.4" y2="1">
      <stop offset="0" stop-color="#6b5a4c"/>
      <stop offset="0.35" stop-color="#4a3128"/>
      <stop offset="0.6" stop-color="#c7b8a6"/>
      <stop offset="0.85" stop-color="#8a6e5e"/>
      <stop offset="1" stop-color="#b55a45"/>
    </linearGradient>
  </defs>

  <!-- paper -->
  <rect class="paper" x="0" y="0" width="867" height="1195"/>

  <!-- top offer tiles -->
  <g class="offer-tiles">
    <polygon class="tile-red" points="0,0 346,0 171,152"/>
    <polygon class="tile-red" points="362,0 706,0 534,152"/>
    <text class="corner-offer corner-offer--white" x="63" y="50">BUY NOW</text>
    <text class="corner-offer corner-offer--yellow" x="420" y="50">PAY LATER</text>
  </g>

  <!-- carpet photo mosaic -->
  <g class="hero-photo">
    <polygon role="img" aria-label="Photo of rolled carpets and shaggy rugs in brown, cream and red tones"
             fill="url(#carpet-tones)"
             points="356,8 706,321 536,493 366,641 181,484 0,321"/>
    <line class="tile-gap" x1="180" y1="170" x2="536" y2="493"/>
    <line class="tile-gap" x1="181" y1="484" x2="530" y2="164"/>
  </g>

  <!-- side tiles -->
  <polygon class="tile-yellow-soft" points="0,346 166,486 0,631"/>
  <polygon class="tile-red-warm" points="716,334 867,472 867,492 716,636 546,486"/>
  <polygon class="tile-yellow" points="536,496 706,651 536,801 362,646"/>
  <polygon class="tile-red" points="706,651 867,796 867,806 713,956 541,801"/>

  <!-- headline -->
  <g class="headline">
    <rect class="title-band" x="140" y="208" width="425" height="82"/>
    <text class="title-pay" x="142" y="283">Pay Weekly</text>
    <text class="title-carpet" x="198" y="366">CARPET</text>
    <text class="title-vinyls" x="302" y="428">&amp; Vinyls</text>
  </g>

  <!-- share note -->
  <g class="share-note-block">
    <text class="share-note share-note--lead" x="845" y="128">Keep This</text>
    <text class="share-note share-note--lead" x="845" y="170">Flyer Safe <tspan class="or">or</tspan></text>
    <text class="share-note share-note--follow" x="845" y="212">Share with</text>
    <text class="share-note share-note--follow" x="838" y="255">your</text>
    <text class="share-note share-note--follow" x="845" y="298">Buddies</text>
  </g>

  <!-- brand -->
  <g class="brand">
    <circle class="tile-red" cx="52" cy="670" r="34"/>
    <text class="brand-name" x="98" y="688">Pallowmere</text>
  </g>

  <!-- welcome tile text -->
  <text class="welcome" x="536" y="620">WELCOME!</text>
  <text class="area" x="528" y="668">WE’RE IN</text>
  <text class="area" x="534" y="713">YOUR AREA</text>

  <!-- urgency tile text -->
  <text class="urgent" x="620" y="762">DON’T</text>
  <text class="urgent" x="622" y="808">MISS IT,</text>
  <text class="save-today" x="620" y="858">SAVE TODAY</text>

  <!-- deals list -->
  <g class="deals">
    <text class="deals-heading" x="118" y="800">CARPET DEALS</text>
    <text class="deals-side" transform="translate(143 1058) rotate(-90)">OUR AMAZING</text>
    <g class="deal-ticks">
      <path class="deal-tick" d="M163 829 l3 3 l5 -6"/>
      <path class="deal-tick" d="M163 864 l3 3 l5 -6"/>
      <path class="deal-tick" d="M163 899 l3 3 l5 -6"/>
      <path class="deal-tick" d="M163 934 l3 3 l5 -6"/>
      <path class="deal-tick" d="M163 968 l3 3 l5 -6"/>
      <path class="deal-tick" d="M163 1003 l3 3 l5 -6"/>
      <path class="deal-tick" d="M163 1038 l3 3 l5 -6"/>
      <path class="deal-tick" d="M163 1073 l3 3 l5 -6"/>
    </g>
    <text class="deal-item" x="180" y="841">Pay only <tspan class="strong">£10.00/week</tspan></text>
    <text class="deal-item" x="180" y="876"><tspan class="strong">£500</tspan> credit limit</text>
    <text class="deal-item" x="180" y="911">Interest <tspan class="strong">FREE</tspan></text>
    <text class="deal-item" x="180" y="946"><tspan class="strong">NO</tspan> Credit Checks</text>
    <text class="deal-item" x="180" y="980">FREE Underlay</text>
    <text class="deal-item" x="180" y="1015">FREE Grippers</text>
    <text class="deal-item" x="180" y="1050">FREE Door Trims</text>
    <text class="deal-item" x="180" y="1085">FREE Home Measuring</text>
  </g>

  <!-- contact footer -->
  <g class="contact">
    <polygon class="tile-red" points="0,1036 156,1195 0,1195"/>
    <polygon class="tile-red" points="867,1066 760,1158 800,1195 867,1195"/>
    <text class="contact-label" x="5" y="1162">CALL US NOW</text>
    <text class="contact-phone" x="147" y="1168">(800) 555-0142</text>
    <text class="contact-web" x="476" y="1170">www.pallowmere.co.uk</text>
    <text class="contact-label" x="784" y="1165">VISIT US</text>
  </g>
</svg>
</body>
</html>
```